依頼詳細
現在、お店のロゴはあります。既存のロゴを使用して、立て看板を新しくしたいと思っています。看板の入稿に必要なデザインをillustratorで作成して頂きたいと思います。
重視するポイントは、
1。概要、特徴にも記載しましたが2Fとわかること。
2.ワインはそうですが、お食事ができること。
3.現在使用しているロゴを看板の中心にもっていってワインと一目でわかるようにしたい
4.現在の立て看板がとてもカジュアルな為、店内の雰囲気とかなりギャップがあります。若年の方が立ち飲みバルや、居酒屋、カフェ等と間違えて誤って入ってこられることがたまにあります。お店の雰囲気がでるようなシンプルで雰囲気のあるデザインを希望します。看板製作会社が、完全データの支給を要求しているため、Adobe Illustratorアウトラインデータ Mac=8.0 Win=CSにて納品お願いします。
お店の雰囲気、現在の看板、ロゴなどは添付ファイル参照ください。
記載項目
店舗名、2F、ワインとお食事、今のロゴ。定番メニューのリスト、電話番号。席数。
希望イメージ
シンプル 複雑
単色 カラフル
暗い 明るい
日常 高級
遊び心 厳粛
未来的 伝統的
女性的 男性的
希望する色
白、ワインレッド系、ロゴに合わせたカラー
納品ファイル
• 高解像度JPG (.jpg)
• イラストレーター形式 (.ai)
補足説明
入口の間口が狭いために、看板に必ず2F+↑を記載していただきたいです。表、左上がり、裏、右上がりの☝をつけてほしいです。現在の立て看板ファイルを参照してください。
看板仕上がりサイズはW600×H900です。【画面有効サイズ】 W530×H830mmとなっています。内側に投光機を設置し、ライトアップされます。宜しくお願いいたします。
■ 選んだ理由

現在の問題点をクリアし、お店の雰囲気が看板一つで出ている所。

■ 提案者全員のお礼・コメント

修正等にご対応いただきまして誠にありがとうございました。今後も名刺の修正等依頼していくつもりですので機会がありましたら是非とも宜しくお願いいたします。

```html
<!DOCTYPE html>
<html lang="ja">
<head>
<meta charset="utf-8">
<title>LUNEVO ワインとお食事 立て看板</title>
<link href="https://fonts.googleapis.com/css2?family=Noto+Sans+JP:wght@400;500;700&family=Yuji+Syuku&display=swap" rel="stylesheet">
<style>
  :root{
    --wine:#9a1c20;
    --brown:#6a3a1f;
    --ink:#4a2a18;
    --paper-top:#fbf8f5;
    --paper-bottom:#cdc6c0;
    --white:#ffffff;
    --icon-tone:#9a9693;
  }
  html,body{margin:0;padding:0;overflow:hidden;background:#e6e1dc;}
  .signboard{
    position:relative;width:767px;height:1200px;overflow:hidden;
    background:linear-gradient(180deg,var(--paper-top) 15%,var(--paper-bottom) 100%);
    font-family:"Noto Sans JP",sans-serif;color:var(--ink);
  }
  .header-wave{position:absolute;left:0;top:0;width:767px;height:230px;}
  .tagline{
    position:absolute;left:44px;top:42px;margin:0;
    font-family:"Yuji Syuku",serif;font-weight:400;font-size:54px;line-height:1;
    color:#3a1a10;letter-spacing:2px;
  }
  .brand{
    position:absolute;left:112px;top:348px;display:flex;align-items:center;gap:26px;
  }
  .brand-dot{width:30px;height:30px;border-radius:50%;background:var(--brown);}
  .brand-name{
    margin:0;font-size:128px;font-weight:500;line-height:1;color:var(--brown);letter-spacing:4px;
  }
  .section-title{
    position:absolute;margin:0;font-size:28px;font-weight:700;line-height:1.2;color:var(--ink);
    border-bottom:3px solid var(--wine);padding-bottom:2px;
  }
  .drink-title{left:44px;top:540px;width:326px;}
  .food-title{left:358px;top:752px;width:345px;text-align:right;}
  .menu{position:absolute;margin:0;padding:0;list-style:none;font-size:17px;color:var(--ink);}
  .menu li{display:flex;justify-content:space-between;line-height:1.3;}
  .drink-menu{left:56px;top:595px;width:335px;}
  .drink-menu li{margin-bottom:13px;}
  .food-menu{left:372px;top:810px;width:331px;}
  .food-menu li{margin-bottom:16px;}
  .food-menu .indent{padding-left:1em;}
  .tableware{
    position:absolute;left:435px;top:583px;width:242px;height:107px;border-radius:10px;
    background:linear-gradient(90deg,#b5b1ad,var(--icon-tone));opacity:.55;
  }
  .seats{
    position:absolute;left:26px;top:758px;width:180px;height:198px;border-radius:16px;
    background:var(--wine);color:var(--white);text-align:center;
    display:flex;flex-direction:column;justify-content:center;
    font-size:28px;font-weight:700;line-height:1.22;
  }
  .seats p{margin:0 0 10px;}
  .seats p:last-child{margin-bottom:0;}
  .contact{position:absolute;left:44px;top:1034px;margin:0;font-size:23px;line-height:38px;color:var(--ink);}
  .floor-mark{position:absolute;left:550px;top:1022px;width:170px;height:128px;}
</style>
</head>
<body>
<div class="signboard">
  <svg class="header-wave" viewBox="0 0 767 230" aria-hidden="true">
    <path d="M0 0H767V55C650 55 560 60 460 72C360 84 260 170 150 168C90 167 40 150 0 142Z" fill="var(--wine)"/>
    <path d="M0 142C40 150 90 167 150 168C260 170 360 84 460 72C560 60 650 55 767 55V86C650 86 560 90 465 102C365 114 265 200 150 198C90 197 40 182 0 174Z" fill="var(--brown)"/>
  </svg>
  <h2 class="tagline">ワインとお食事</h2>

  <div class="brand">
    <span class="brand-dot"></span>
    <h1 class="brand-name">LUNEVO</h1>
  </div>

  <h3 class="section-title drink-title">Drink</h3>
  <ul class="menu drink-menu">
    <li><span>グラスシャンパーニュ</span><span>1300yen〜</span></li>
    <li><span>グラススパークリング</span><span>950yen〜</span></li>
    <li><span>グラスワイン（赤・白）</span><span>各種 900yen〜</span></li>
  </ul>
  <div class="tableware" role="img" aria-label="ワイングラスと皿、ナイフとフォークのイラスト"></div>

  <div class="seats">
    <p>カウンター<br>7席</p>
    <p>テーブル<br>10席</p>
  </div>

  <h3 class="section-title food-title">Food</h3>
  <ul class="menu food-menu">
    <li><span>秋刀魚のアクア・パッツア</span><span>900yen</span></li>
    <li><span>ポークと野菜の<br><span class="indent">南イタリア風煮込</span></span><span style="align-self:flex-end">1,300yen</span></li>
    <li><span>ラザニア</span><span>1,400yen</span></li>
  </ul>

  <p class="contact">営業時間／18：00〜24：00（L.O 23：00）<br>お問合わせ／090-4812-7730<br>http://www.lunevo-wine.com/</p>

  <svg class="floor-mark" viewBox="0 0 170 128" aria-label="2階">
    <path d="M4 122H38V94H70V66H102V38H136" fill="none" stroke="var(--ink)" stroke-width="6"/>
    <path d="M4 110H26V82H58V54H90V26H124" fill="none" stroke="var(--ink)" stroke-width="3"/>
    <text x="112" y="116" font-family="Noto Sans JP,sans-serif" font-weight="700" font-size="48" fill="var(--ink)">2F</text>
  </svg>
</div>
</body>
</html>
```